Veranaxis Business Card and Letter Head

We are a leadership assessment consultancy based in Sydney, Australia. We help executive-level decison-makers select leaders for more senior level roles in corporate and government organisations. Our methodology is based on the latest research from the field of neuroscience.
We need a business card design and matching letter head that presents our company, Veranaxis, as a:
1. trusted adviser to senior executive-level decison makers
2. niche consultancy who are experts in the field of assessing leadership talent
3. results-focused solution provider who balance scientific methods with pragmatic solutions
The following company details should be used in all designs:
Company Name: Veranaxis
Details (for business card):
Daniel Prescott
Lead Assessment Advisor
Level 29, Brenning Tower
7 Brenning Square
Sydney, NSW 2000 Australia
Phone: 1300 482 716
Mobile: 0412 573 208
Email: daniel.prescott@veranaxis.com.au
Website: veranaxis.com.au
I have attached the logo for Veranaxis (for both a white and black background) - your business card and letter head designs must incoporate this logo and colour scheme.
Thanks for your interest in this project, I'm looking forward to receiving your ideas.
Regards,
Daniel
Executive-level decison-makers in corporate and government organisations (e.g., CEO, VP, Head of Human Resources)
Leadership

```html
<!DOCTYPE html>
<html lang="en">
<head>
<meta charset="utf-8">
<title>Veranaxis Stationery</title>
<link href="https://fonts.googleapis.com/css2?family=Arimo:wght@400;700&display=swap" rel="stylesheet">
<style>
  :root {
    --paper: #ffffff;
    --backdrop: #ffffff;
    --ink: #1c1c1c;
    --band-dark: #1d1d1d;
    --brand-red: #c0140f;
    --muted: #6f6f6f;
    --url-grey: #6a6a6a;
    --on-dark: #f2f2f2;
  }
  * { box-sizing: border-box; margin: 0; padding: 0; }
  html, body {
    width: 900px; height: 1200px; overflow: hidden;
    background: var(--backdrop);
    font-family: "Arimo", Arial, sans-serif;
    color: var(--ink);
  }
  .stationery { position: relative; width: 900px; height: 1200px; }

  /* Letterhead */
  .letterhead {
    position: absolute; left: 33px; top: 62px; width: 744px; height: 1053px;
    background: var(--paper);
    box-shadow: 2px 3px 8px rgba(0,0,0,0.28);
  }
  .brand { position: absolute; display: flex; align-items: center; }
  .brand-square { background: var(--brand-red); flex: none; }
  .brand-name { font-weight: 700; color: var(--ink); letter-spacing: -0.5px; line-height: 1; }
  .brand-tagline {
    position: absolute; color: var(--muted); text-transform: uppercase;
    letter-spacing: 0.3px; white-space: nowrap;
  }
  .letterhead .brand { left: 392px; top: 45px; }
  .letterhead .brand-square { width: 56px; height: 56px; margin-right: 14px; }
  .letterhead .brand-name { font-size: 46px; }
  .letterhead .brand-tagline { left: 475px; top: 94px; font-size: 12.5px; letter-spacing: 0.6px; }

  .letterhead-footer { position: absolute; left: 0; right: 0; bottom: 0; height: 142px; }
  .red-rule { height: 14px; background: var(--brand-red); }
  .dark-band { background: var(--band-dark); }
  .letterhead-footer .dark-band { height: 128px; text-align: center; color: var(--on-dark); }
  .footer-contact { padding-top: 7px; font-size: 10.5px; line-height: 16px; }
  .web-address { color: var(--url-grey); white-space: nowrap; letter-spacing: 0.5px; line-height: 1; }
  .letterhead-footer .web-address { font-size: 63px; margin-top: 2px; }

  /* Business card */
  .business-card {
    position: absolute; left: 515px; top: 537px; width: 353px; height: 215px;
    background: var(--paper);
    box-shadow: 2px 3px 8px rgba(0,0,0,0.35);
  }
  .business-card .brand { left: 163px; top: 19px; }
  .business-card .brand-square { width: 36px; height: 36px; margin-right: 8px; }
  .business-card .brand-name { font-size: 27px; }
  .business-card .brand-tagline { left: 207px; top: 49px; font-size: 7px; }
  .cardholder { position: absolute; left: 20px; top: 85px; font-size: 13.5px; white-space: nowrap; }
  .cardholder-title { font-size: 8.5px; color: var(--muted); margin-left: 2px; }
  .card-footer { position: absolute; left: 0; right: 0; bottom: 0; height: 107px; }
  .card-footer .red-rule { height: 8px; }
  .card-footer .dark-band { height: 99px; position: relative; color: var(--on-dark); }
  .card-address, .card-contact {
    position: absolute; top: 12px; font-size: 9.5px; line-height: 12.5px; white-space: nowrap;
  }
  .card-address { left: 20px; }
  .card-contact { left: 171px; }
  .card-footer .web-address { position: absolute; left: 20px; top: 58px; font-size: 30px; letter-spacing: 0.3px; }
</style>
</head>
<body>
<main class="stationery">
  <section class="letterhead" aria-label="Letterhead">
    <header class="brand">
      <span class="brand-square"></span>
      <span class="brand-name">Veranaxis</span>
    </header>
    <p class="brand-tagline">Assessing Tomorrow's Leaders</p>

    <footer class="letterhead-footer">
      <div class="red-rule"></div>
      <div class="dark-band">
        <p class="footer-contact">
          Level 29, Brenning Tower, 7 Brenning Square, Sydney NSW 2000 Australia<br>
          P: 1300 482 716&nbsp; M: 0412 573 208&nbsp; E: daniel.prescott@veranaxis.com.au
        </p>
        <p class="web-address">www.veranaxis.com.au</p>
      </div>
    </footer>
  </section>

  <section class="business-card" aria-label="Business card">
    <header class="brand">
      <span class="brand-square"></span>
      <span class="brand-name">Veranaxis</span>
    </header>
    <p class="brand-tagline">Assessing Tomorrow's Leaders</p>
    <p class="cardholder">Daniel Prescott <span class="cardholder-title">Lead Assessment Advisor</span></p>

    <footer class="card-footer">
      <div class="red-rule"></div>
      <div class="dark-band">
        <p class="card-address">Level 29, Brenning Tower<br>7 Brenning Square<br>Sydney NSW 2000 Australia</p>
        <p class="card-contact">P: 1300 482 716<br>M: 0412 573 208<br>E: daniel.prescott@veranaxis.com.au</p>
        <p class="web-address">www.veranaxis.com.au</p>
      </div>
    </footer>
  </section>
</main>
</body>
</html>
```